Logo & Visitenkarte für Mentoring  und Supervision
Logo & Visitenkarte für Mentoring und Supervision
Zielgruppe
Ich gehe für eine neue verkörperte weibliche Spiritualität.
Ich biete Mentoring und Supervision für Mädchen und Frauen an.
Ich halte Raum für Mädchen und Frauenkreise, Retreate und Fortbildungen.
Ich halte die Vision von einem Yogini-Dorf und bin dabei eine Stiftung zu gründen.
Meine Zielgruppe: Mädchen und Frauen, die verbunden mit Himmel und Erde selbstermächtigt ihr Leben leben und ihre ganz spezielle Gabe in die Welt bringen: ganz schön stark
Aufgabenstellung
Ganzheit. Schönheit. Stärke
sollen in diesem sehr weiblichen Raum für Mädchen und Frauen ausgestrahlt werden.
Frauenzeichen und Raum verbinden

```html
<!DOCTYPE html>
<html lang="de">
<head>
<meta charset="utf-8">
<title>Marlene Vogt – Visitenkarte</title>
<link href="https://fonts.googleapis.com/css2?family=Montserrat:wght@500;600&display=swap" rel="stylesheet">
<style>
  :root {
    --plum: #5c0a2c;
    --red: #c4161c;
    --gold-light: #f2d488;
    --gold: #e4a63a;
    --gold-deep: #d4870f;
    --page: #ffffff;
    --card: #ffffff;
  }
  * { margin: 0; padding: 0; box-sizing: border-box; }
  html, body {
    width: 1200px; height: 1199px; overflow: hidden;
    background: var(--page);
    font-family: "Montserrat", sans-serif;
  }
  .card {
    position: absolute; left: 311px; width: 585px; height: 379px;
    background: var(--card); overflow: hidden;
    box-shadow: 0 0 0 1px #eee;
  }
  .card--front { top: 136px; }
  .card--back { top: 672px; }

  .brand-disc {
    position: absolute; left: 191px; top: 53px; width: 202px; height: 202px;
    border-radius: 50%;
    background: radial-gradient(circle at 50% 40%, var(--gold-light), var(--gold) 70%, var(--gold-deep));
  }
  .brand-name {
    position: absolute; left: 0; right: 0; text-align: center;
    color: var(--plum); font-weight: 600; letter-spacing: 0.5px;
  }
  .card--front .brand-name { top: 252px; font-size: 44px; }
  .tagline {
    position: absolute; left: 0; right: 0; text-align: center;
    font-weight: 600; font-size: 16.5px; color: var(--plum);
  }
  .card--front .tagline { top: 318px; }
  .dot { color: var(--red); }

  .card--back .brand-name { top: 22px; font-size: 40px; }
  .services {
    position: absolute; left: 0; right: 0; top: 85px; text-align: center;
    color: var(--red); font-weight: 500; font-size: 16.5px;
  }
  .contact {
    position: absolute; left: 0; right: 0; top: 131px; text-align: center;
    color: var(--plum); font-weight: 500; font-size: 18.5px; line-height: 1.35;
  }
  .contact .address { margin-bottom: 10px; }
  .contact .phone { margin-bottom: 6px; }
  .band { position: absolute; left: 0; top: 0; width: 585px; height: 379px; }
</style>
</head>
<body>
  <section class="card card--front">
    <div class="brand-disc"></div>
    <div class="brand-name">Marlene Vogt</div>
    <div class="tagline">Raum für Ganzheit <span class="dot">•</span> Schönheit <span class="dot">•</span> Stärke</div>
  </section>

  <section class="card card--back">
    <svg class="band" viewBox="0 0 585 379" aria-hidden="true">
      <defs>
        <linearGradient id="goldBand" x1="0" y1="0" x2="0" y2="1">
          <stop offset="0.55" stop-color="var(--gold-light)"/>
          <stop offset="1" stop-color="var(--gold-deep)"/>
        </linearGradient>
      </defs>
      <path d="M0,212 Q292,462 585,212 L585,379 L0,379 Z" fill="url(#goldBand)"/>
    </svg>
    <div class="brand-name">Marlene Vogt</div>
    <div class="services">Mentoring <span>•</span> Tempel <span>•</span> Projekte für Mädchen und Frauen</div>
    <div class="contact">
      <div class="address">Am Weidenhang 4 <span class="dot">•</span> 21379 Lindenau/Klein Moor</div>
      <div class="phone">0151&nbsp; 24 63 807</div>
      <div>info@marlene-vogt.de</div>
      <div>www.marlene-vogt.de</div>
    </div>
  </section>
</body>
</html>
```